Business Card and Simple Logo Desgin

New Zealand based start up company "Brook Advisory LTD" requires business cards and simple logo design.

Card Content.

Brook Advisory LTD

Joanna Pritchard
CA, BMS (Hons)

j.pritchard@brookadvisory.co.nz
PH +64 21 574 160

Target Market(s)

Corporate Business in IT, Finance and accounting.

Industry/Entity Type

Business

```html
<!DOCTYPE html>
<html lang="en">
<head>
<meta charset="utf-8">
<title>Brook Advisory LTD – Business Card</title>
<link href="https://fonts.googleapis.com/css2?family=Source+Sans+3:wght@400;600;700&display=swap" rel="stylesheet">
<style>
  :root {
    --card-black: #000000;
    --card-edge: #6e6e6e;
    --brand-orange: #ff6a10;
    --brand-white: #ffffff;
    --text-grey: #d4d4d4;
    --page-bg: #ffffff;
  }
  * { margin: 0; padding: 0; box-sizing: border-box; }
  html, body {
    width: 1200px;
    height: 696px;
    overflow: hidden;
    background: var(--page-bg);
  }
  .card {
    position: relative;
    width: 1200px;
    height: 696px;
    background: var(--card-black);
    border: 2px solid var(--card-edge);
    font-family: "Source Sans 3", "Myriad Pro", Arial, sans-serif;
    overflow: hidden;
  }
  .info-column {
    position: absolute;
    left: 0;
    top: 0;
    width: 760px;
    height: 100%;
    text-align: center;
  }
  .brand-mark {
    position: absolute;
    left: 0;
    top: 118px;
    width: 760px;
    display: flex;
    justify-content: center;
    align-items: center;
    gap: 22px;
  }
  .brand-mark__dot {
    width: 30px;
    height: 30px;
    border-radius: 50%;
    background: var(--brand-orange);
  }
  .brand-mark__name {
    color: var(--brand-white);
    font-size: 104px;
    font-weight: 400;
    line-height: 1;
    letter-spacing: -1px;
  }
  .company-name {
    position: absolute;
    left: 0;
    top: 318px;
    width: 760px;
    color: var(--brand-orange);
    font-size: 45px;
    font-weight: 700;
    line-height: 1;
    letter-spacing: 0.2px;
    text-transform: uppercase;
  }
  .contact {
    position: absolute;
    left: 0;
    width: 760px;
    color: var(--text-grey);
    line-height: 1;
  }
  .contact--name { top: 446px; font-size: 32px; font-weight: 700; }
  .contact--quals { top: 494px; font-size: 34px; font-weight: 400; }
  .contact--email { top: 560px; font-size: 32px; font-weight: 400; }
  .contact--phone { top: 610px; font-size: 33px; font-weight: 400; }
  .side-band {
    position: absolute;
    left: 1046px;
    top: 0;
    width: 60px;
    height: 100%;
    background: linear-gradient(90deg, #2a1206 0%, #7a3309 50%, #2a1206 100%);
  }
</style>
</head>
<body>
  <main class="card">
    <section class="info-column">
      <div class="brand-mark">
        <span class="brand-mark__dot"></span>
        <span class="brand-mark__name">Brook</span>
      </div>
      <h1 class="company-name">Brook Advisory LTD</h1>
      <p class="contact contact--name">Joanna Pritchard</p>
      <p class="contact contact--quals">CA, BMS (Hons)</p>
      <p class="contact contact--email">j.pritchard@brookadvisory.co.nz</p>
      <p class="contact contact--phone">PH +64 21 574 160</p>
    </section>
    <div class="side-band" role="img" aria-label="Decorative vertical band of orange lines with white dots"></div>
  </main>
</body>
</html>
```